"Lomi's" Website Design

Lomi's makes earth friendly, healthy, and delicious snacks that are completely gluten free. We are looking for a website that is easy to navigate, energetic, and conveys our purpose "To create healthy, earth-friendly, gluten free snacks that fill bellies and warm hearts."
Our first product is "Lomi's Crunch Rockets" are a small, square, cracker pack with an unreasonable amount of cheddar cheese flavor. The flavor literally explodes in your mouth!
We really want our site to pop and show off some personality.
I'm attaching the logo for the company, feel free to go beyond the logo in terms of color.
Here are some sites that we like!
http://www.frostvale-example.com/company
http://www.pebblemeal-example.com/
http://www.qv47-example.com/
http://www.dorsetloaf-example.com/
http://www.ventobite-example.com/food/products_zest/
http://www.marvelscoop-example.com/

```html
<!DOCTYPE html>
<html lang="en">
<head>
<meta charset="utf-8">
<title>Lomi's</title>
<link rel="stylesheet" href="https://fonts.googleapis.com/css2?family=Dosis:wght@300;400&family=Open+Sans:wght@400;600&display=swap">
<style>
:root{
  --brown:#3f2102;
  --brown-field:#4a2a06;
  --orange:#ff5a1c;
  --cream:#f3f3f3;
  --panel:#e9e9e9;
  --text:#666;
  --white:#fff;
  --muted:#6e5232;
  --bread:#e6cf9c;
  --bread-deep:#c9a466;
  --filling:#e2b95a;
}
*{box-sizing:border-box;margin:0;padding:0}
html,body{width:1075px;height:1200px;overflow:hidden}
body{position:relative;background:var(--cream);font-family:"Open Sans",sans-serif;color:var(--text)}
.abs{position:absolute}
.site-header{left:0;top:0;width:1075px;height:116px;background:var(--brown)}
.brand{left:74px;top:12px;font-family:"Dosis",sans-serif;font-weight:400;font-size:72px;line-height:1;color:var(--orange)}
.search{left:587px;top:27px;width:226px;height:24px;border-radius:5px;background:#552d05;color:#a98a66;font-size:11px;padding:5px 11px}
.phone-top{left:831px;top:20px;font-family:"Dosis",sans-serif;font-weight:300;font-size:27px;color:var(--white)}
.nav a{position:absolute;top:72px;font-family:"Dosis",sans-serif;font-weight:300;font-size:21px;color:var(--white);text-decoration:none}
.nav a.active{color:var(--orange)}
.slider-band{left:0;top:116px;width:1075px;height:388px;background:var(--brown-field)}
.slide{left:77px;top:116px;width:919px;height:388px;
  background:
    radial-gradient(ellipse 30% 60% at 26% 40%,var(--bread),transparent 70%),
    radial-gradient(ellipse 22% 70% at 86% 50%,#ecd6a4,transparent 70%),
    radial-gradient(ellipse 25% 55% at 58% 55%,var(--filling),transparent 75%),
    linear-gradient(100deg,#d9bd83,var(--bread-deep) 45%,#d4b070 70%,#cfae72)}
.slide-arrow{width:32px;height:32px}
.showcase{left:0;top:504px;width:1075px;height:433px;background:linear-gradient(#f7f7f7,#e6e6e6 40%,#fafafa)}
.bump{left:512px;top:480px;width:48px;height:48px;border-radius:50%;background:var(--orange);clip-path:inset(24px 0 0 0)}
.ornament{left:466px;top:526px;width:140px;height:10px;border-radius:5px;background:#e0e0e0}
.panel{left:108px;top:566px;width:858px;height:343px;background:var(--panel);border:1px solid var(--white);box-shadow:0 0 2px #ccc}
.tab{position:absolute;top:557px;height:32px;background:var(--orange);color:var(--white);font-family:"Dosis",sans-serif;font-weight:300;font-size:21px;text-align:center;line-height:32px;box-shadow:0 1px 2px rgba(0,0,0,.25)}
.tab::before,.tab::after{content:"";position:absolute;top:0;border-bottom:8px solid #3a2a20}
.tab::before{left:-6px;border-left:6px solid transparent}
.tab::after{right:-6px;border-right:6px solid transparent}
.card{position:absolute;top:604px;width:250px}
.card-photo{width:250px;height:136px;border:4px solid var(--white);box-shadow:0 0 2px #bbb}
.card p{margin:8px 2px 0;font-size:9.9px;line-height:16px;text-align:justify;color:var(--text)}
.btn{display:inline-block;margin-top:15px;margin-left:5px;width:87px;height:29px;background:#4a4a4a;border:1px solid #2c2c2c;box-shadow:inset 0 1px 0 #777;color:#eee;font-size:11.5px;text-align:center;line-height:27px}
.site-footer{left:0;top:937px;width:1075px;height:263px;background:var(--brown)}
.foot-title{position:absolute;top:963px;font-family:"Dosis",sans-serif;font-weight:300;font-size:21px;color:var(--white)}
.tweet{left:91px;top:1003px;width:180px;height:123px;border:1px solid #6b4a25;border-radius:3px;padding:23px 14px 0;font-size:8.6px;line-height:16px;color:var(--white);text-align:justify}
.tweet::after{content:"";position:absolute;left:38px;bottom:-7px;width:12px;height:12px;background:var(--brown);border-right:1px solid #6b4a25;border-bottom:1px solid #6b4a25;transform:rotate(45deg)}
.follow{left:178px;top:1131px;font-size:11px;color:#d8c2a0}
.post{position:absolute;left:333px}
.post-thumb{width:54px;height:54px;border:3px solid #150a00}
.post h4{position:absolute;left:70px;top:2px;font-weight:400;font-size:14.5px;color:var(--white);white-space:nowrap}
.post time{position:absolute;left:70px;top:23px;font-size:11px;color:var(--muted);white-space:nowrap}
.map{left:556px;top:1004px;width:177px;height:180px;border:4px solid #150a00;background:linear-gradient(135deg,#c9d7e8,#f2e6b8 55%,#b6c9e0)}
.social{position:absolute;top:1005px;width:22px;height:22px;border-radius:3px;background:var(--orange)}
.contact-row{position:absolute;left:783px;display:flex;align-items:center;gap:16px;font-size:13.5px;color:var(--white)}
.contact-row svg{width:15px;height:18px}
</style>
</head>
<body>
<header class="site-header abs">
  <div class="brand abs">Lomi's</div>
  <div class="search abs">Search</div>
  <div class="phone-top abs">(XXX) XXX XXXX</div>
  <nav class="nav">
    <a class="active" style="left:518px">Home</a>
    <a style="left:643px">About us</a>
    <a style="left:784px">Products</a>
    <a style="left:927px">Contact</a>
  </nav>
</header>

<div class="slider-band abs" role="img" aria-label="Dark brown damask background pattern"></div>
<div class="slide abs" role="img" aria-label="Close-up photo of golden bread rolls filled with savoury chicken, cheese and green pepper"></div>
<svg class="slide-arrow abs" style="left:95px;top:289px" viewBox="0 0 32 32"><circle cx="16" cy="16" r="16" fill="#2d2a25"/><path d="M19 9 L11 16 L19 23Z" fill="#e0a020"/></svg>
<svg class="slide-arrow abs" style="left:944px;top:289px" viewBox="0 0 32 32"><circle cx="16" cy="16" r="16" fill="#2d2a25"/><path d="M13 9 L21 16 L13 23Z" fill="#e0a020"/></svg>

<section class="showcase abs"></section>
<div class="bump abs"></div>
<svg class="abs" style="left:528px;top:503px" width="16" height="8" viewBox="0 0 16 8"><path d="M3 7 L8 2 L13 7Z" fill="#fff" opacity=".8"/></svg>
<div class="ornament abs" role="img" aria-label="Decorative scroll flourish"></div>
<div class="panel abs"></div>

<div class="tab" style="left:161px;width:178px">WELCOME</div>
<div class="tab" style="left:466px;width:139px">PRODUCTS</div>
<div class="tab" style="left:744px;width:152px">BRANDS</div>

<article class="card" style="left:125px">
  <div class="card-photo" style="background:linear-gradient(120deg,#8a5a2a,#d8b890 50%,#a03020)" role="img" aria-label="Photo of breaded snack bites cut open"></div>
  <p>Lorem Ipsum is simply dummy text of the printing and typesetting industry. Lorem Ipsum has been the industry's standard dummy text ever since the 1500s, when an unknown printer took a galley of type and scrambled it to makebook.</p>
  <span class="btn">Read more</span>
</article>
<article class="card" style="left:410px">
  <div class="card-photo" style="background:linear-gradient(120deg,#7a5a1a,#c8a040 45%,#d8d8a0)" role="img" aria-label="Photo of fried pastry with a pickle filling"></div>
  <p>Lorem Ipsum is simply dummy text of the printing and typesetting industry. Lorem Ipsum has been the industry's standard dummy text ever since the 1500s, when an unknown printer took a galley of type and scrambled it to makebook.</p>
  <span class="btn">Read more</span>
</article>
<article class="card" style="left:695px">
  <div class="card-photo" style="background:linear-gradient(120deg,#e06a1a,#f0a040 50%,#f2dca0)" role="img" aria-label="Photo of a crispy orange cheese snack"></div>
  <p>Lorem Ipsum is simply dummy text of the printing and typesetting industry. Lorem Ipsum has been the industry's standard dummy text ever since the 1500s, when an unknown printer took a galley of type and scrambled it to makebook.</p>
  <span class="btn">Read more</span>
</article>

<footer class="site-footer abs"></footer>
<h3 class="foot-title" style="left:92px">Our Tweets</h3>
<h3 class="foot-title" style="left:333px">Latest Posts</h3>
<h3 class="foot-title" style="left:556px">Location</h3>
<h3 class="foot-title" style="left:782px">Contact Us</h3>

<div class="tweet abs">Lorem Ipsum is simply dummy text of the printing and typesetting industry. Lorem Ipsum has been the industry standard dummy text ever since the 1500s...</div>
<div class="follow abs">follow on Chirpline....</div>

<div class="post" style="top:1004px"><div class="post-thumb" style="background:linear-gradient(#6a4a2a,#b08050)" role="img" aria-label="Photo of a restaurant interior"></div><h4>Lorem Lipsum</h4><time>May 05, 2012</time></div>
<div class="post" style="top:1068px"><div class="post-thumb" style="background:linear-gradient(#222,#888)" role="img" aria-label="Black and white photo"></div><h4>Lorem Lipsum</h4><time>May 05, 2012</time></div>
<div class="post" style="top:1132px"><div class="post-thumb" style="background:linear-gradient(#1a2a4a,#c03040)" role="img" aria-label="Photo of colourful round objects"></div><h4>Lorem Lipsum</h4><time>May 05, 2012</time></div>

<div class="map abs" role="img" aria-label="Street map showing the shop location"></div>

<span class="social" style="left:782px"></span>
<span class="social" style="left:817px"></span>
<span class="social" style="left:851px"></span>
<span class="social" style="left:887px"></span>
<span class="social" style="left:923px"></span>

<div class="contact-row" style="top:1045px"><svg viewBox="0 0 15 18"><path d="M3 1 L6 1 L7 5 L5 7 Q7 11 10 13 L12 11 L15 13 L15 16 Q13 18 10 17 Q3 13 1 5 Q1 2 3 1Z" fill="#ddd"/></svg>(XXX) XXX XXXX</div>
<div class="contact-row" style="top:1077px"><svg viewBox="0 0 15 18"><rect x="0.5" y="4.5" width="14" height="10" fill="none" stroke="#ddd"/><path d="M0.5 4.5 L7.5 10 L14.5 4.5" fill="none" stroke="#ddd"/></svg>Email</div>
<div class="contact-row" style="top:1107px"><svg viewBox="0 0 15 18"><path d="M7.5 1 A5 5 0 0 1 12.5 6 Q12.5 10 7.5 17 Q2.5 10 2.5 6 A5 5 0 0 1 7.5 1Z" fill="#ddd"/><circle cx="7.5" cy="6" r="2" fill="#3f2102"/></svg>Address</div>
</body>
</html>
```